Remedial massage therapist or clinical look

I would like a plain white or light colour background with front view of a musculoskeletal human body on the from on the left hand side, with Mirela Tostani remedial and sports massage therapist. On the back I want the back view of the musculoskeletal body on the left side with Mirela Tostani remedial and sports massage therapist, my contact details and appointment time and date. The colour of writing can be the same or close colour to the musculoskeletal body.
I don't want it to look to busy but also don't want it to be to plain,

Industry/Entity Type

Massage

Contact Information for Business Card

Mirela Tostani
Remedial and Sports Massage Therapist
Contact number: 0481536207
Email: tostanimirela41@quillmail.example

```html
<!DOCTYPE html>
<html lang="en">
<head>
<meta charset="utf-8">
<title>Mirela Tostani – Remedial and Sports Massage Therapist</title>
<link rel="stylesheet" href="https://fonts.googleapis.com/css2?family=Open+Sans:ital,wght@0,400;0,600;0,700;1,400&display=swap">
<style>
  :root {
    --paper: #ffffff;
    --ink: #111111;
    --band-red: #c8230f;
    --band-yellow: #f2d321;
    --muscle-red: #c8341e;
    --muscle-deep: #9e2414;
    --bone-yellow: #d9cf3a;
  }
  html, body {
    margin: 0;
    padding: 0;
    overflow: hidden;
    background: var(--paper);
  }
  .card {
    position: relative;
    width: 1200px;
    height: 693px;
    background: var(--paper);
    overflow: hidden;
    font-family: "Open Sans", sans-serif;
    color: var(--ink);
  }
  .band {
    position: absolute;
    right: 0;
    height: 11px;
    box-shadow: 2px 3px 3px rgba(0,0,0,0.35);
  }
  .band--red { left: 384px; top: 47px; background: var(--band-red); }
  .band--yellow { left: 579px; top: 71px; background: var(--band-yellow); }
  .anatomy-figure {
    position: absolute;
    left: 132px;
    top: 62px;
    width: 258px;
    height: 578px;
    border-radius: 120px 120px 40px 40px;
    background: linear-gradient(90deg, var(--muscle-red) 0%, var(--muscle-deep) 35%, var(--bone-yellow) 55%, var(--muscle-red) 80%);
  }
  .details {
    position: absolute;
    right: 54px;
    top: 0;
    text-align: right;
  }
  .name {
    position: absolute;
    right: 0;
    top: 226px;
    margin: 0;
    font-size: 48px;
    font-weight: 600;
    white-space: nowrap;
    text-shadow: 3px 3px 3px rgba(0,0,0,0.35);
  }
  .role {
    position: absolute;
    right: 0;
    top: 302px;
    margin: 0;
    font-size: 30px;
    font-style: italic;
    white-space: nowrap;
  }
  .contact {
    position: absolute;
    right: 0;
    margin: 0;
    font-size: 30px;
    white-space: nowrap;
  }
  .contact--phone { top: 415px; }
  .contact--email { top: 480px; }
  .contact strong { font-weight: 700; font-size: 33px; }
</style>
</head>
<body>
<div class="card">
  <div class="band band--red"></div>
  <div class="band band--yellow"></div>
  <div class="anatomy-figure" role="img" aria-label="Front view illustration of a musculoskeletal human body, half muscles and half skeleton"></div>
  <div class="details">
    <h1 class="name">Mirela Tostani</h1>
    <p class="role">Remedial and Sports Massage Therapist</p>
    <p class="contact contact--phone">Contact number: <strong>0481536207</strong></p>
    <p class="contact contact--email">Email: <strong>tostanimirela41@quillmail.example</strong></p>
  </div>
</div>
</body>
</html>
```